Corporate PowerPoint design for edtech focused on developing world / emerging markets

I am involved in a edtech startup focused on providing financial literacy for students and young adults in the developing world and emerging markets; currently focus will be on Africa. We are in discussions with the CEO of a bank in S. Africa and would deploy products throughout much of Africa with them. I need a corporate powerpoint that I can use for my customers and for investor presentation. Company name is Tidecrest, which is a surfing term; meant to connotate movement and energy.
Updates

Target Market(s)

target market is two fold - will be selling to execs at banks and telecommunications companies; also need to present to investors.

Industry/Entity Type

Financial

Font styles to use
Sans Serif

Requirements
Must have
• I'd like to have a slide or two that allow me to do columns for things like feature / benefits or just content that doesn't run left to right across the entire powepoint page.
• otherwise, too much color (other than white) uses a ton of ink, so I don't want a full color background e.g. I don't want a blue or green background. I would like to provide some standard corporate info at the bottom - just basics of contact info, url and ability to change them as necessary

```html
<!DOCTYPE html>
<html lang="en">
<head>
<meta charset="utf-8">
<title>Tidecrest – Corporate Slide Template</title>
<link rel="stylesheet" href="https://fonts.googleapis.com/css2?family=Carlito:wght@400;700&display=swap">
<style>
  :root{
    --backdrop:#5f5f61;
    --slide:#ffffff;
    --ink:#1c1c1c;
    --teal:#1a9ea0;
    --brand:#17808f;
    --rule:#8a8a8a;
    --wave:#f1f1f1;
    --ring:#9a9a9a;
  }
  *{box-sizing:border-box;margin:0;padding:0}
  html,body{width:1200px;height:839px;overflow:hidden}
  body{background:var(--backdrop);font-family:"Carlito","Calibri",Arial,sans-serif;color:var(--ink);position:relative}
  .slide{position:absolute;background:var(--slide);overflow:hidden}
  .slide--title{left:37px;top:37px;width:541px;height:388px}
  .slide--intro{left:616px;top:37px;width:518px;height:388px}
  .slide--team{left:338px;top:449px;width:498px;height:373px}
  .wave-deco{position:absolute;left:-60px;top:-40px;width:340px;height:420px;
    background:radial-gradient(ellipse at 40% 45%,var(--wave) 0%,rgba(241,241,241,.6) 45%,rgba(255,255,255,0) 72%)}
  .abs{position:absolute}
  .wordmark{position:absolute;font-weight:700;color:var(--brand);letter-spacing:.5px;display:flex;align-items:center;white-space:nowrap}
  .wordmark .dot{display:inline-block;border-radius:50%;background:var(--brand);margin-left:6px}
  .slide--title .wordmark{left:59px;top:154px;font-size:33px}
  .slide--title .wordmark .dot{width:26px;height:26px}
  .pres-title{left:308px;top:211px;font-size:16px;letter-spacing:.3px}
  .pres-name{right:33px;top:236px;font-size:11px;letter-spacing:.3px}
  .pres-date{right:40px;top:256px;font-size:11px}
  .pres-url{right:45px;top:361px;font-size:13px}
  .heading{font-size:16px;letter-spacing:.3px}
  .heading strong{color:var(--teal);font-weight:700}
  .slide--intro .heading{left:58px;top:38px}
  .intro-text{left:32px;top:136px;width:240px;font-size:10.6px;line-height:13.6px;text-align:justify}
  .growth-photo{left:279px;top:123px;width:239px;height:172px;
    background:radial-gradient(ellipse at 55% 78%,#c49a5c 0%,#b8905a 30%,rgba(255,255,255,0) 62%),
      radial-gradient(ellipse at 55% 30%,#5f9f3a 0%,rgba(95,159,58,.55) 30%,rgba(255,255,255,0) 58%)}
  .footer-mark{font-size:17px}
  .footer-mark .dot{width:14px;height:14px;margin-left:4px}
  .slide--intro .footer-mark{left:16px;top:341px}
  .footer-rule{height:1px;background:var(--rule)}
  .slide--intro .footer-rule{left:164px;right:0;top:354px}
  .page-no{font-size:12px}
  .slide--intro .page-no{left:488px;top:365px}
  .slide--team .heading{left:55px;top:37px}
  .team{left:70px;top:80px;display:flex;gap:24px}
  .member{width:80px;text-align:center}
  .portrait-ring{width:76px;height:76px;margin:0 auto;border:1px solid var(--ring);border-radius:50%;padding:5px}
  .portrait{width:100%;height:100%;border-radius:50%;background:radial-gradient(circle at 50% 40%,#d9c3b0 0%,#8f8a86 55%,#3b4150 100%)}
  .member-name{margin-top:12px;font-size:12px}
  .member-role{font-size:9px;font-weight:700;margin-top:1px}
  .member-bio{font-size:8px;line-height:10.5px;margin-top:11px}
  .slide--team .footer-mark{left:15px;top:330px}
  .slide--team .footer-rule{left:159px;right:0;top:340px}
  .slide--team .page-no{left:470px;top:350px}
</style>
</head>
<body>

<section class="slide slide--title">
  <div class="wave-deco" role="img" aria-label="Faint wave decoration"></div>
  <div class="wordmark">TIDECREST<span class="dot"></span></div>
  <p class="abs pres-title">PRESENTATION TITLE HERE</p>
  <p class="abs pres-name">NAME OF THE PRESENTEE</p>
  <p class="abs pres-date">FEB 2015</p>
  <p class="abs pres-url">www.tidecrest-site.example</p>
</section>

<section class="slide slide--intro">
  <div class="wave-deco" role="img" aria-label="Faint wave decoration"></div>
  <h2 class="abs heading">INTRODUCTION OF <strong>THE COMPANY</strong></h2>
  <p class="abs intro-text">Ask the basic questions as you define and allocate tasks (workload/complexity, dependencies, time to complete, fit with capabilities). Make sure the workload is balanced and allocated fairly&nbsp; Ask the basic questions as you define and allocate tasks (workload/complexity, dependencies, time to complete, fit with capabilities). Make sure the workload is balanced and allocated fairly</p>
  <div class="abs growth-photo" role="img" aria-label="Photo of a young green plant growing from a pile of coins"></div>
  <div class="wordmark footer-mark">TIDECREST<span class="dot"></span></div>
  <div class="abs footer-rule"></div>
  <p class="abs page-no">01</p>
</section>

<section class="slide slide--team">
  <div class="wave-deco" role="img" aria-label="Faint wave decoration"></div>
  <h2 class="abs heading">ABOUT <strong>US</strong></h2>
  <div class="abs team">
    <article class="member">
      <div class="portrait-ring"><div class="portrait" role="img" aria-label="Portrait photo of Johnson"></div></div>
      <p class="member-name">Johnson</p>
      <p class="member-role">His designation</p>
      <p class="member-bio">Ask the basic questions as you define and allocate tasks (workload/complexity</p>
    </article>
    <article class="member">
      <div class="portrait-ring"><div class="portrait" role="img" aria-label="Portrait photo of Peter"></div></div>
      <p class="member-name">Peter</p>
      <p class="member-role">His designation</p>
      <p class="member-bio">Ask the basic questions as you define and allocate tasks (workload/complexity</p>
    </article>
    <article class="member">
      <div class="portrait-ring"><div class="portrait" role="img" aria-label="Portrait photo of Park"></div></div>
      <p class="member-name">Park</p>
      <p class="member-role">His designation</p>
      <p class="member-bio">Ask the basic questions as you define and allocate tasks (workload/complexity</p>
    </article>
    <article class="member">
      <div class="portrait-ring"><div class="portrait" role="img" aria-label="Portrait photo of James"></div></div>
      <p class="member-name">James</p>
      <p class="member-role">His designation</p>
      <p class="member-bio">Ask the basic questions as you define and allocate tasks (workload/complexity</p>
    </article>
  </div>
  <div class="wordmark footer-mark">TIDECREST<span class="dot"></span></div>
  <div class="abs footer-rule"></div>
  <p class="abs page-no">02</p>
</section>

</body>
</html>
```